Business Card Design

I need a business card design for a new business based in South West Australia.
I specialize in residential window cleaning & general handyman maintenance.

Industry/Entity Type

Business

Contact Information for Business Card

Dale Marsh - 512 SILVER HAWK DETAILING
- Window Cleaning
- House Maintenance

```html
<!DOCTYPE html>
<html lang="en">
<head>
<meta charset="utf-8">
<title>Dale Marsh – Business Card</title>
<link rel="stylesheet" href="https://fonts.googleapis.com/css2?family=Open+Sans:wght@600&family=Montserrat:wght@500;700&display=swap">
<style>
  :root {
    --backdrop: #bfe5d8;
    --card-light: #f4f7fd;
    --card-mid: #d9e3f6;
    --card-deep: #c3d2ef;
    --name-blue: #1f7fab;
    --tag-blue: #3d9cc9;
    --phone-blue: #3f6690;
    --service-blue: #2c92c4;
  }
  html, body {
    margin: 0;
    width: 1200px;
    height: 856px;
    overflow: hidden;
    background: var(--backdrop);
  }
  .canvas {
    position: relative;
    width: 1200px;
    height: 856px;
    display: flex;
    align-items: center;
    justify-content: center;
  }
  .business-card {
    position: relative;
    width: 840px;
    height: 480px;
    border-radius: 44px;
    overflow: hidden;
    box-shadow: 0 18px 40px rgba(40, 90, 80, 0.18);
  }
  .card-pattern {
    position: absolute;
    inset: 0;
    background:
      linear-gradient(180deg, rgba(255,255,255,0.55) 0%, rgba(255,255,255,0) 40%, rgba(255,255,255,0.4) 100%),
      linear-gradient(135deg, var(--card-light) 0%, var(--card-mid) 45%, var(--card-deep) 100%);
  }
  .card-content {
    position: absolute;
    inset: 0;
  }
  .owner-name {
    position: absolute;
    top: 58px;
    right: 110px;
    margin: 0;
    font-family: "Open Sans", sans-serif;
    font-weight: 600;
    font-size: 92px;
    line-height: 1;
    letter-spacing: 1px;
    color: var(--name-blue);
  }
  .business-name {
    position: absolute;
    top: 168px;
    right: 122px;
    margin: 0;
    font-family: "Montserrat", sans-serif;
    font-weight: 700;
    font-size: 17px;
    letter-spacing: 3.5px;
    color: var(--tag-blue);
  }
  .phone {
    position: absolute;
    top: 232px;
    left: 360px;
    display: flex;
    align-items: center;
    gap: 14px;
    font-family: "Montserrat", sans-serif;
    font-weight: 500;
    font-size: 34px;
    letter-spacing: 3px;
    color: var(--phone-blue);
  }
  .phone-icon { width: 18px; height: 30px; }
  .services {
    position: absolute;
    bottom: 62px;
    left: 60px;
    right: 60px;
    margin: 0;
    padding: 0;
    list-style: none;
    display: flex;
    justify-content: space-between;
    font-family: "Montserrat", sans-serif;
    font-weight: 700;
    font-size: 26px;
    letter-spacing: 3.5px;
    color: var(--service-blue);
  }
  .services li::before { content: "•"; margin-right: 6px; }
</style>
</head>
<body>
  <main class="canvas">
    <article class="business-card">
      <div class="card-pattern" role="img" aria-label="Pale blue diagonal lattice pattern covering the card face"></div>
      <div class="card-content">
        <h1 class="owner-name">Dale Marsh</h1>
        <p class="business-name">512 SILVER HAWK DETAILING</p>
        <div class="phone">
          <svg class="phone-icon" viewBox="0 0 18 30" aria-hidden="true">
            <rect x="1.5" y="1.5" width="15" height="27" rx="3" fill="none" stroke="currentColor" stroke-width="2.4"/>
            <line x1="7" y1="24" x2="11" y2="24" stroke="currentColor" stroke-width="2.4" stroke-linecap="round"/>
          </svg>
          <span>0487215604</span>
        </div>
        <ul class="services">
          <li>Window Cleaning</li>
          <li>House Maintenance</li>
        </ul>
      </div>
    </article>
  </main>
</body>
</html>
```